3 Flyer Project: Industrial, Civil, and Commercial

Total of 3 separate flyers that go together to be put in folders for marketing. The three flyer categories will be Industrial, Civil, and Commercial. I will upload three photos for each flyer and verbiage for each flyer. The photos may change upon final revisions. We want creativity and not just bullet points on a page.

FLYER #1 INDUSTRIAL

INDUSTRIAL EXPERIENCE:
BRELLANT COMPANY
VESKAR
OAKMOOR PIT MINE
GALDWYN FORGE STEEL
PERNOTH QUARTZWORKS
DUNMARROW VALE LOOP RAILWAY

INDUSTRIAL FOCUS AREAS:
PLANT FACILITY WATER SYSTEMS
HEAVY CONCRETE
FACILITY REPAIR
INDUSTRIAL UPGRADES
RAILWAYS AND MANUFACTURING

INDUSTRIAL SOLUTIONS:
WE MAINTAIN AN EXTENSIVE LEVEL OF DETAIL AND INNOVATIVE PROBLEM-SOLVING TALENTS TO DELIVER HIGH QUALITY, SUSTAINABLE SOLUTIONS.

FLYER #2 CIVIL

CIVIL EXPERIENCE:
VELDORAN DEPT. OF TRANSPORTATION
KESTRIA DEPT. OF TRANSPORTATION
PLOVENDA DEPT. OF TRANSPORTATION
BUREAU OF WORKSMITHS
NATIONAL SKYWAYS AUTHORITY BOARD
MINISTRY OF GUARDIANSHIP

CIVIL FOCUS AREAS:
AIRFIELD
STREETSCAPES
STORM DRAINAGE
UTILITY UPGRADES
BOX CULVERTS
RETAINING WALLS

CIVIL SOLUTIONS:
WE SPECIALIZE IN COMPLEX CIVIL PROJECTS.

FLYER #3 COMMERCIAL

COMMERCIAL EXPERIENCE:
HOLLENBRAKE UPLANDS UNIVERSITY
VELDORAN OFFICE OF STRUCTURES
TOWN OF BRANWICK, MISSISSIPPI
TOWN OF MERRODA, MISSISSIPPI
ACADEMY FOR ADVANCED STUDIES

COMMERCIAL FOCUS AREAS:
NEW CONSTRUCTION
RENOVATIONS
STRUCTURAL FOUNDATIONS
STRUCTURAL UPGRADES

COMMERCIAL SOLUTIONS:
WE NOT ONLY KNOW HOW ALL THE PARTS AND PIECES FIT TOGETHER WITHIN A PROJECT, BUT WE SPECIALIZE IN THE SELF PERFORMANCE OF MANY DIVISIONS WHICH DIFFERENTIATES US FROM MANY OTHER GENERAL CONTRACTORS.

Marketing

• 3 photos on each flyer based on the Industrial, Commercial, and Civil flyers description. Our company logo as well as descriptions shown for each flyer. The blue we use in our logo cmyk is 100-80-0-22

```html
<!DOCTYPE html>
<html lang="en">
<head>
<meta charset="utf-8">
<title>Harlow Construction – Industrial, Civil and Commercial Flyers</title>
<link href="https://fonts.googleapis.com/css2?family=Oswald:wght@500;600&family=Lato:wght@400;700&display=swap" rel="stylesheet">
<style>
  :root {
    --brand-blue: #1d3591;
    --ink: #141414;
    --text: #2a2a2a;
    --paper: #ffffff;
    --backdrop: #5b5c5e;
    --url-grey: #3a3a3a;
  }
  * { box-sizing: border-box; margin: 0; padding: 0; }
  html, body { width: 1200px; height: 800px; overflow: hidden; }
  body { background: var(--backdrop); font-family: "Lato", Arial, sans-serif; position: relative; }

  .flyer {
    position: absolute; top: 138px; width: 358px; height: 506px;
    background: linear-gradient(180deg, #fff 0%, #fff 50%, #eef0f3 78%, #f4f5f7 100%);
    overflow: hidden;
  }
  .flyer--industrial { left: 38px; }
  .flyer--civil { left: 423px; }
  .flyer--commercial { left: 806px; }

  .title-block {
    position: absolute; left: 0; top: 0; width: 166px; height: 54px;
    background: var(--brand-blue); color: #fff;
    font-family: "Oswald", "Arial Narrow", sans-serif; font-weight: 600;
    font-size: 31px; line-height: 54px; letter-spacing: 0.2px;
    display: flex; align-items: center; justify-content: center;
  }
  .title-rail { position: absolute; left: 0; top: 54px; width: 11px; height: 82px; background: var(--brand-blue); }

  .brand { position: absolute; left: 192px; top: 9px; display: flex; align-items: center; gap: 6px; color: var(--brand-blue); font-family: "Oswald", "Arial Narrow", sans-serif; font-weight: 500; }
  .brand__mark { width: 28px; height: 28px; background: var(--brand-blue); }
  .brand__name { display: flex; flex-direction: column; line-height: 1; }
  .brand__word { font-size: 25px; letter-spacing: 0.5px; }
  .brand__sub { font-size: 10.5px; letter-spacing: 1.2px; margin-top: 2px; }

  .hero { position: absolute; left: 15px; top: 60px; width: 330px; height: 178px; }
  .hero-shadow-side { position: absolute; left: 350px; top: 126px; width: 8px; height: 128px; background: var(--ink); }
  .hero-shadow-base { position: absolute; left: 222px; top: 242px; width: 136px; height: 12px; background: var(--ink); }

  .thumb { position: absolute; left: 22px; width: 89px; height: 73px; box-shadow: 4px 4px 0 var(--ink); }
  .thumb::before {
    content: ""; position: absolute; left: -7px; top: -6px; width: 68px; height: 48px;
    border-top: 3px solid var(--brand-blue); border-left: 3px solid var(--brand-blue); z-index: -1;
  }
  .thumb-wrap { position: absolute; inset: 0; z-index: 1; }
  .thumb--upper { top: 263px; }
  .thumb--lower { top: 355px; }

  .info { position: absolute; left: 136px; right: 10px; z-index: 2; }
  .info__heading {
    font-family: "Oswald", "Arial Narrow", sans-serif; font-weight: 500;
    color: var(--brand-blue); font-size: 9.5px; letter-spacing: 0.1px; margin-bottom: 6px;
  }
  .info__list { list-style: none; display: grid; column-gap: 8px; row-gap: 5px; font-size: 7.2px; color: var(--text); }
  .info__list li { position: relative; padding-left: 8px; white-space: nowrap; }
  .info__list li::before { content: ""; position: absolute; left: 0; top: 2.6px; width: 3px; height: 3px; border-radius: 50%; background: var(--brand-blue); }
  .cols-1 { grid-template-columns: 1fr; }
  .cols-2 { grid-template-columns: auto auto; justify-content: start; }
  .cols-3 { grid-template-columns: auto auto auto; justify-content: start; }

  .solutions {
    position: absolute; left: 0; top: 438px; width: 358px; height: 37px;
    background: var(--brand-blue); color: #fff; display: flex; align-items: center; justify-content: center; gap: 10px; padding: 0 12px;
  }
  .solutions__label { font-family: "Oswald", "Arial Narrow", sans-serif; font-weight: 500; font-size: 9.5px; white-space: nowrap; }
  .solutions__text { font-size: 7px; line-height: 1.25; }
  .solutions__text--large { font-size: 10px; }

  .footer { position: absolute; left: 0; top: 475px; width: 358px; height: 31px; display: flex; background: var(--paper); }
  .footer__email { width: 160px; background: var(--ink); color: #fff; font-size: 8.5px; display: flex; align-items: center; justify-content: center; }
  .footer__url { flex: 1; display: flex; align-items: center; justify-content: center; color: var(--url-grey); font-size: 8px; letter-spacing: 2.4px; }
</style>
</head>
<body>

<!-- Industrial -->
<article class="flyer flyer--industrial">
  <div class="title-block">INDUSTRIAL</div>
  <div class="title-rail"></div>
  <div class="brand"><span class="brand__mark"></span><span class="brand__name"><span class="brand__word">HARLOW</span><span class="brand__sub">CONSTRUCTION</span></span></div>
  <div class="hero-shadow-side"></div><div class="hero-shadow-base"></div>
  <div class="hero" role="img" aria-label="Power plant with cooling towers behind a grassy field" style="background:linear-gradient(180deg,#a9c0d8 0%,#d9dde0 35%,#9a9688 52%,#6f8a4a 62%,#577a35 100%)"></div>
  <div class="thumb thumb--upper"><div class="thumb-wrap" role="img" aria-label="Night construction site with heavy equipment" style="background:linear-gradient(180deg,#1d1d22 0%,#3b3833 60%,#6d6354 100%)"></div></div>
  <div class="thumb thumb--lower"><div class="thumb-wrap" role="img" aria-label="Concrete formwork and rebar in an excavation" style="background:linear-gradient(180deg,#7c9fc4 0%,#bdb9a6 35%,#8c6a46 65%,#6d5036 100%)"></div></div>
  <section class="info" style="top:289px">
    <h2 class="info__heading">INDUSTRIAL EXPERIENCE:</h2>
    <ul class="info__list cols-2">
      <li>Brellant company</li><li>Galdwyn forge steel</li>
      <li>Veskar</li><li>Pernoth quartzworks</li>
      <li>Oakmoor pit mine</li><li>Dunmarrow vale loop railway</li>
    </ul>
  </section>
  <section class="info" style="top:365px;left:138px">
    <h2 class="info__heading">INDUSTRIAL FOCUS AREAS:</h2>
    <ul class="info__list cols-2">
      <li>Plant facility water systems</li><li>Industrial upgrades</li>
      <li>Heavy concrete</li><li>Railways and manufacturing</li>
      <li>Facility repair</li>
    </ul>
  </section>
  <div class="solutions">
    <span class="solutions__label">INDUSTRIAL SOLUTIONS:</span>
    <p class="solutions__text">We maintain an extensive level of detail and innovative problem-solving talents to deliver high quality, sustainable solutions.</p>
  </div>
  <footer class="footer"><span class="footer__email">info@harlowconstruction.com</span><span class="footer__url">www.harlowconstruction.com</span></footer>
</article>

<!-- Civil -->
<article class="flyer flyer--civil">
  <div class="title-block">CIVIL</div>
  <div class="title-rail"></div>
  <div class="brand"><span class="brand__mark"></span><span class="brand__name"><span class="brand__word">HARLOW</span><span class="brand__sub">CONSTRUCTION</span></span></div>
  <div class="hero-shadow-side"></div><div class="hero-shadow-base"></div>
  <div class="hero" role="img" aria-label="Small town intersection with brick paved street and old storefronts" style="background:linear-gradient(180deg,#9fb6cf 0%,#d5d6d2 30%,#a89e8c 55%,#b8836a 75%,#a86a56 100%)"></div>
  <div class="thumb thumb--upper"><div class="thumb-wrap" role="img" aria-label="New roadway lined with young trees" style="background:linear-gradient(180deg,#b9cfe1 0%,#8aa86a 45%,#5b8a3b 62%,#8b8f8c 80%,#5c8a3a 100%)"></div></div>
  <div class="thumb thumb--lower"><div class="thumb-wrap" role="img" aria-label="Aircraft parked on a concrete airfield apron" style="background:linear-gradient(180deg,#c9d6e2 0%,#e4e6e8 40%,#b9bcbf 60%,#d2d3d1 100%)"></div></div>
  <section class="info" style="top:277px">
    <h2 class="info__heading">CIVIL EXPERIENCE:</h2>
    <ul class="info__list cols-1">
      <li>Veldoran dept. of transportation</li>
      <li>Kestria dept. of transportation</li>
      <li>Plovenda dept. of transportation</li>
      <li>Bureau of worksmiths</li>
      <li>National skyways authority board</li>
      <li>Ministry of guardianship</li>
    </ul>
  </section>
  <section class="info" style="top:383px">
    <h2 class="info__heading">CIVIL FOCUS AREAS:</h2>
    <ul class="info__list cols-3" style="column-gap:14px">
      <li>Airfield</li><li>Storm drainage</li><li>Box culverts</li>
      <li>Streetscapes</li><li>Utility upgrades</li><li>Retaining walls</li>
    </ul>
  </section>
  <div class="solutions">
    <span class="solutions__label">CIVIL SOLUTIONS:</span>
    <p class="solutions__text solutions__text--large">We specialize in complex civil projects.</p>
  </div>
  <footer class="footer"><span class="footer__email">info@harlowconstruction.com</span><span class="footer__url">www.harlowconstruction.com</span></footer>
</article>

<!-- Commercial -->
<article class="flyer flyer--commercial">
  <div class="title-block">COMMERCIAL</div>
  <div class="title-rail"></div>
  <div class="brand"><span class="brand__mark"></span><span class="brand__name"><span class="brand__word">HARLOW</span><span class="brand__sub">CONSTRUCTION</span></span></div>
  <div class="hero-shadow-side"></div><div class="hero-shadow-base"></div>
  <div class="hero" role="img" aria-label="Red brick university building under renovation" style="background:linear-gradient(180deg,#5e98d4 0%,#a9c8e6 28%,#b4543f 48%,#9a3f30 75%,#b8a48c 100%)"></div>
  <div class="thumb thumb--upper"><div class="thumb-wrap" role="img" aria-label="Outdoor amphitheater stage on a lawn" style="background:linear-gradient(180deg,#6fa5d8 0%,#c7d6e1 35%,#8d7a66 55%,#7aa04e 72%,#a9bf6e 100%)"></div></div>
  <div class="thumb thumb--lower"><div class="thumb-wrap" role="img" aria-label="Bronze sculpture on a paved plaza" style="background:linear-gradient(180deg,#8fb2d6 0%,#7b9b5f 40%,#6e5b45 60%,#a88764 100%)"></div></div>
  <section class="info" style="top:288px">
    <h2 class="info__heading">COMMERCIAL EXPERIENCE:</h2>
    <ul class="info__list cols-1">
      <li>Hollenbrake uplands university</li>
      <li>Veldoran office of structures</li>
      <li>Town of branwick, mississippi</li>
      <li>Town of merroda, mississippi</li>
      <li>Academy for advanced studies</li>
    </ul>
  </section>
  <section class="info" style="top:383px;left:138px">
    <h2 class="info__heading">COMMERCIAL FOCUS AREAS:</h2>
    <ul class="info__list cols-2" style="column-gap:24px">
      <li>New construction</li><li>Structural foundations</li>
      <li>Renovations</li><li>Structural upgrades</li>
    </ul>
  </section>
  <div class="solutions">
    <span class="solutions__label">COMMERCIAL SOLUTIONS:</span>
    <p class="solutions__text">We not only know how all the parts and pieces fit together within a project, but we specialize in the self performance of many divisions which differentiates us from many other general contractors.</p>
  </div>
  <footer class="footer"><span class="footer__email">info@harlowconstruction.com</span><span class="footer__url">www.harlowconstruction.com</span></footer>
</article>

</body>
</html>
```